Publisher needs a book cover design for ‘Lanterns Over the Marsh Gate’ book

We need a book cover (front, back, spine) for the 2nd edition of a book entitled ‘Lanterns Over the Marsh Gate’ and subtitled ‘the quiet geography of tidal winds, ferry routes and harbour lanterns’ (inverted commas not to be part of the title and subtitle). The author is Rupert Calloway. The publisher is Vellmark Press. The finished size of the paperback version will be the industry standard 9" x 6". There will be paperback, hardback, and e-book versions. The final number of pages is expected to be in the region 150-180 pages. Text for the back cover is not yet available, but at the bottom of the back cover should be publisher logo (rectangular) on the left and space for the ISBN bar code on the right. The circular logo should be on the spine. The design should be original and not include any stock images that have been created by someone else or may require obtaining a copyright licence to use. Symbols in common use and not copyrighted are probably ok. There are no required images, photographs or symbols except the publisher logo at the left bottom of the back cover and lower spine. Spine lettering should be UK/US style with the top of the writing nearest the front cover. The designer is free to be creative using appropriate diagrams, symbols or abstract designs. Rectangular and circular variants of the publisher logo are attached. Designers are assured that when evaluating designs absolutely no notice whatsoever is taken of a designer's Pixo Rally ranking or status; We are completely output driven, so what matters is the design, not the ranking or status of the designer. In a similar way, designs are not evaluated as 'good' or 'bad' - the winning design will be chosen after review by a design review panel and is not decided arbitrarily by a single person. All submitted designs should be capable of effective copyright assignment.

Target Market(s)

Practitioners, parents, teachers, pupils and academics concerned with child protection, safeguarding and the elimination of emotional abuse of children in the classroom

Font styles to use
Serif
Sans Serif

Requirements
Must have
• • Title, author, edition, subtitle, publisher logo
Nice to have
• • Originality, innovation
Should not have
• • Stock images or anything else requiring additional copyright discussions and negotiations.

```html
<!DOCTYPE html>
<html lang="en">
<head>
<meta charset="utf-8">
<title>Lanterns Over the Marsh Gate — Cover</title>
<link href="https://fonts.googleapis.com/css2?family=EB+Garamond:wght@400;600&family=Arimo&display=swap" rel="stylesheet">
<style>
  :root {
    --backdrop: #ecebf3;
    --paper: #ffffff;
    --paper-shade: #e9e9ea;
    --ink: #1d1b1c;
    --tag: #141414;
    --tag-text: #ffffff;
    --pink-light: #ff9cf6;
    --pink-mid: #f46cf0;
    --pink-deep: #d83ee0;
    --rule: #d9d9d9;
  }
  * { box-sizing: border-box; margin: 0; padding: 0; }
  html, body { width: 1200px; height: 865px; overflow: hidden; }
  body { background: var(--backdrop); font-family: "EB Garamond", Georgia, serif; color: var(--ink); }

  .cover {
    position: absolute; left: 62px; top: 65px; width: 1076px; height: 735px;
    background: var(--paper);
    box-shadow: 0 2px 10px rgba(0,0,0,0.12);
  }

  /* Back panel */
  .back {
    position: absolute; left: 0; top: 0; width: 489px; height: 100%;
    background: linear-gradient(160deg, var(--paper-shade) 0%, var(--paper) 35%);
  }
  .blurb {
    position: absolute; left: 46px; top: 55px; width: 410px;
    font-size: 14.6px; line-height: 21.3px;
  }
  .about-heading {
    position: absolute; left: 46px; top: 370px;
    font-size: 15px; font-weight: 600; text-decoration: underline;
  }
  .about-text {
    position: absolute; left: 46px; top: 390px; width: 410px;
    font-size: 14.6px; line-height: 20.2px;
  }
  .about-text .wrap-gap { float: right; width: 104px; height: 96px; }
  .photo-box {
    position: absolute; left: 363px; top: 366px; width: 94px; height: 115px;
    border: 1px solid var(--ink); background: var(--paper);
    display: flex; align-items: center; justify-content: center;
    font-family: "Arimo", Arial, sans-serif; font-size: 20px;
  }
  .isbn-space {
    position: absolute; left: 315px; top: 631px; width: 153px; height: 49px;
    border: 1px solid var(--ink); background: var(--paper);
  }
  .publisher-mark {
    position: absolute; left: 337px; top: 690px;
    display: flex; align-items: center; gap: 5px;
    font-size: 15px; letter-spacing: 0.5px;
  }
  .publisher-mark .dot { width: 22px; height: 22px; border-radius: 50%; background: var(--ink); }

  /* Spine */
  .spine {
    position: absolute; left: 489px; top: 0; width: 86px; height: 100%;
    border-left: 1px solid var(--rule); border-right: 1px solid var(--rule);
  }
  .spine-title {
    position: absolute; left: 50%; top: 60px; transform: translateX(-50%);
    writing-mode: vertical-rl; white-space: nowrap;
    display: flex; align-items: center; gap: 6px;
  }
  .spine-title .small { font-size: 18px; letter-spacing: 1.5px; }
  .spine-title .large { font-size: 40px; letter-spacing: 1px; line-height: 1; }
  .spine-author {
    position: absolute; left: 50%; top: 560px; transform: translateX(-50%);
    writing-mode: vertical-rl; font-size: 15px; white-space: nowrap;
  }
  .spine-mark {
    position: absolute; left: 50%; top: 680px; transform: translateX(-50%);
    display: flex; flex-direction: column; align-items: center; gap: 3px;
  }
  .spine-mark .dot { width: 28px; height: 28px; border-radius: 50%; background: var(--ink); }
  .spine-mark .name { font-size: 8px; letter-spacing: 0.5px; }

  /* Edition tag spanning spine and front */
  .edition-tag {
    position: absolute; left: 489px; top: 22px; width: 180px; height: 20px;
    background: var(--tag); color: var(--tag-text);
    display: flex; font-size: 13px; line-height: 20px;
  }
  .edition-tag span { flex: 0 0 auto; }
  .edition-tag .spine-part { width: 86px; text-align: center; }
  .edition-tag .front-part { width: 94px; text-align: center; }

  /* Front */
  .front { position: absolute; left: 575px; top: 0; width: 501px; height: 100%; }
  .front-art {
    position: absolute; left: 0; top: 0; width: 100%; height: 327px;
    background:
      radial-gradient(ellipse at 50% 55%, var(--pink-light) 0%, transparent 60%),
      linear-gradient(180deg, var(--pink-light) 0%, var(--pink-mid) 55%, var(--pink-deep) 100%);
  }
  .front-title {
    position: absolute; left: 0; top: 238px; width: 100%; text-align: center;
  }
  .front-title .small { display: block; font-size: 32px; letter-spacing: 1px; line-height: 40px; }
  .front-title .large { display: block; font-size: 68px; line-height: 76px; letter-spacing: 1px; }
  .subtitle {
    position: absolute; left: 0; top: 504px; width: 100%; text-align: center;
    font-size: 18px; line-height: 18px;
  }
  .author {
    position: absolute; left: 0; top: 683px; width: 100%; text-align: center;
    font-size: 19px;
  }
</style>
</head>
<body>
<div class="cover">
  <section class="back">
    <p class="blurb">So far, the agendas for child protection, safeguarding, and the safer recruitment of people working with children have been driven mainly by a small number of very high profile and shocking cases involving physical abuse, sexual abuse, or neglect. Those cases have invariably highlighted failures in established procedures that are supposed to prevent these things from happening. The resulting initiatives have put a great deal of effort into reforming relevant social work and law agencies, and how they work together. However, as a consequence of most focus being placed on those cases because of huge media and political pressure, other issues have not received the attention they need. Emotional abuse can have a profound, long-lasting impact on a child, as can emotional well-being.</p>
    <h2 class="about-heading">About Author</h2>
    <p class="about-text"><span class="wrap-gap"></span>The classroom environment can have an impact well into adulthood. Most adults have experienced emotional abuse in some classroom at some time In a similar way, a positive classroom environment can also lead to life-long happy memories. Research results are clear about all of this. What research is not so clear about is the extent to which teachers may realize their effect but there is no doubts that good and bad teachers leave a life-long mark.</p>
    <div class="photo-box">Photo</div>
    <div class="isbn-space"></div>
    <div class="publisher-mark"><span class="dot"></span><span>VELLMARK PRESS</span></div>
  </section>

  <section class="spine">
    <div class="spine-title">
      <span class="small">LANTERNS OVER THE</span>
      <span class="large">MARSH GATE</span>
    </div>
    <div class="spine-author">Rupert Calloway</div>
    <div class="spine-mark"><span class="dot"></span><span class="name">VELLMARK</span></div>
  </section>

  <section class="front">
    <div class="front-art" role="img" aria-label="Soft-focus pink toned scene behind the title"></div>
    <h1 class="front-title">
      <span class="small">LANTERNS OVER THE</span>
      <span class="large">MARSH GATE</span>
    </h1>
    <p class="subtitle">The quiet geography of tidal winds,<br>ferry routes and harbour lanterns</p>
    <p class="author">Rupert Calloway</p>
  </section>

  <div class="edition-tag"><span class="spine-part">2nd Edition</span><span class="front-part">2nd Edition</span></div>
</div>
</body>
</html>
```